Business Card Update, need to bring life to the card, two sided color

We need a new business card design, are moving and changing addresses and need a new look, we have the logos already attached but need a new style moving forward. Can incorporate the color of the logo (The Green) as well, maybe a solid back? We deal with safety products revolving around static electricity and safety lighting. Would like to keep same font in second logo as well.

Target Market(s)

Electrical Safety, Lighting

Contact Information for Business Card

Lars Whitcombe
Vice President
Office: 555-284-7316
Cell: 555-862-0457
lars@tkwhitcombe.com
www.tkwhitcombe.com
4700 West Cedar Boulevard
Suite #320
Roswell, GA 30412

Font styles to use
Serif
Sans Serif

Requirements
Must have
• Since 1918
Nice to have
• Could use the 100 Year Logo for back of card, would like the back of card to be the same green as logo.
Should not have
• No black cards please.

```html
<!DOCTYPE html>
<html lang="en">
<head>
<meta charset="utf-8">
<title>T.K. Whitcombe – Business Card</title>
<link rel="stylesheet" href="https://fonts.googleapis.com/css2?family=Montserrat:wght@700;800&family=Open+Sans:wght@400;600&display=swap">
<style>
  :root {
    --brand-green: #0b9a5d;
    --brand-green-soft: #1fa86c;
    --paper: #ffffff;
    --ink: #2b2b2b;
    --stage: #e9ecea;
  }
  * { margin: 0; padding: 0; box-sizing: border-box; }
  html, body { width: 1200px; height: 852px; overflow: hidden; background: var(--stage); }
  .canvas {
    width: 1200px; height: 852px;
    display: flex; align-items: center; justify-content: center; gap: 32px;
  }
  .card {
    position: relative; width: 560px; height: 320px;
    border-radius: 18px; overflow: hidden;
    box-shadow: 0 10px 28px rgba(0,0,0,.18);
  }
  /* Back side */
  .card-back { background: var(--brand-green); }
  .card-back .faint-mark {
    position: absolute; left: 250px; top: 20px;
    width: 280px; height: 280px; border-radius: 50%;
    background: var(--brand-green-soft);
  }
  .card-back .brand {
    position: absolute; left: 40px; top: 118px;
    display: flex; align-items: center; gap: 16px;
  }
  .card-back .brand-dot {
    width: 72px; height: 72px; border-radius: 50%;
    border: 5px solid var(--paper); flex: none;
  }
  .brand-name {
    font-family: "Montserrat", sans-serif; font-weight: 800;
    font-size: 30px; line-height: 1; letter-spacing: .2px;
  }
  .brand-sub {
    font-family: "Montserrat", sans-serif; font-weight: 700;
    font-size: 13px; margin-top: 5px; letter-spacing: .3px;
  }
  .since {
    font-family: "Montserrat", sans-serif; font-weight: 700;
    font-size: 12px; margin-top: 6px; letter-spacing: 2px; text-transform: uppercase;
  }
  .card-back .brand-name, .card-back .brand-sub, .card-back .since { color: var(--paper); }

  /* Front side */
  .card-front { background: var(--paper); }
  .card-front .company { position: absolute; left: 36px; top: 34px; }
  .card-front .brand-name { font-size: 26px; color: var(--brand-green); }
  .card-front .brand-sub { font-size: 11.5px; color: var(--brand-green); margin-top: 4px; }
  .card-front .mark {
    position: absolute; right: 28px; top: 50px;
    width: 220px; height: 220px; border-radius: 50%;
    background: var(--brand-green);
    display: flex; align-items: center; justify-content: center;
  }
  .card-front .mark span {
    font-family: "Montserrat", sans-serif; font-weight: 800;
    font-size: 24px; color: var(--paper); text-align: center; line-height: 1.15;
  }
  .person { position: absolute; left: 36px; top: 102px; font-family: "Open Sans", sans-serif; }
  .person-name {
    font-family: "Montserrat", sans-serif; font-weight: 700;
    font-size: 18px; color: var(--brand-green);
  }
  .person-title { font-size: 13px; color: var(--ink); margin-top: 1px; }
  .address {
    font-family: "Open Sans", sans-serif; position: absolute; left: 36px; top: 156px;
    font-size: 12.5px; color: var(--ink); line-height: 1.4;
  }
  .contact {
    position: absolute; left: 36px; top: 218px; list-style: none;
    font-family: "Open Sans", sans-serif; font-size: 12.5px; color: var(--ink); line-height: 1.5;
  }
  .contact li { display: flex; align-items: center; gap: 8px; }
  .contact svg { width: 12px; height: 12px; flex: none; fill: none; stroke: var(--brand-green); stroke-width: 2; }
  .contact .label { color: var(--brand-green); font-weight: 600; }
  .contact .web-domain { color: var(--brand-green); }
</style>
</head>
<body>
<main class="canvas">
  <section class="card card-back" aria-label="Card back">
    <div class="faint-mark" aria-hidden="true"></div>
    <div class="brand">
      <div class="brand-dot" aria-hidden="true"></div>
      <div>
        <div class="brand-name">T.K. Whitcombe</div>
        <div class="brand-sub">Manufacturing Company, Inc.</div>
        <div class="since">Since 1918</div>
      </div>
    </div>
  </section>

  <section class="card card-front" aria-label="Card front">
    <div class="company">
      <div class="brand-name">T.K. Whitcombe</div>
      <div class="brand-sub">Manufacturing Company, Inc.</div>
    </div>
    <div class="mark"><span>T.K.<br>Whitcombe</span></div>
    <div class="person">
      <div class="person-name">Lars Whitcombe</div>
      <div class="person-title">Vice President</div>
    </div>
    <div class="address">4700 West Cedar Boulevard<br>Suite #320<br>Roswell, GA 30412</div>
    <ul class="contact">
      <li><svg viewBox="0 0 12 12"><path d="M2 1.5l2 .2.8 2.3-1.2 1a6 6 0 0 0 3.4 3.4l1-1.2 2.3.8.2 2a1 1 0 0 1-1.1 1A9 9 0 0 1 1 2.6a1 1 0 0 1 1-1.1z"/></svg><span><span class="label">O</span> 555-284-7316</span></li>
      <li><svg viewBox="0 0 12 12"><path d="M2 1.5l2 .2.8 2.3-1.2 1a6 6 0 0 0 3.4 3.4l1-1.2 2.3.8.2 2a1 1 0 0 1-1.1 1A9 9 0 0 1 1 2.6a1 1 0 0 1 1-1.1z"/></svg><span><span class="label">C</span> 555-862-0457</span></li>
      <li><svg viewBox="0 0 12 12"><rect x="1" y="2.5" width="10" height="7" rx="1"/><path d="M1 3l5 4 5-4"/></svg><span>lars@tkwhitcombe.com</span></li>
      <li><svg viewBox="0 0 12 12"><circle cx="6" cy="6" r="5"/><path d="M1 6h10M6 1c2.5 3 2.5 7 0 10M6 1c-2.5 3-2.5 7 0 10"/></svg><span>www.<span class="web-domain">tkwhitcombe.com</span></span></li>
    </ul>
  </section>
</main>
</body>
</html>
```